Business Cards Design for the electrical wholesaler: clean bold dynamic :)

We need a business card design that would follow our latest brand guidelines. As an electrical wholesaler we want to bring a fresh look and feel into the industry. The design should be clean bold and dynamic. It should come alive with the renewed energy of our green colour. Our grey colour should keep things balanced and complement the notion of maturity and responsibility. We employ Lato as a corporate font however are not bound by this font and we’re open to interpretation here.

Target Market(s)

Electrical contractors

Industry/Entity Type

Business

Contact Information for Business Card

Logo
Name & Surname: Olena Dovbush
Job Title: Director of Marketing
Email: helen.dovbush@mailvane.example
Cell phone: XXX.XXX.XXXX
Address: 20917 - 87 Ave. Edmonton, AB, Canada. T6K 2R8
Business Phone: 780.555.0187
Website: www.qorvil.example

Font styles to use
Other font styles liked:
• Lato

Requirements
Must have
• Logo & website
Nice to have
• Brand elements - some of them you may find in the attached Brand Guidelines (e.g. three lines on the background signifying "W")

```html
<!DOCTYPE html>
<html lang="en">
<head>
<meta charset="utf-8">
<title>Qorvil Business Card</title>
<link href="https://fonts.googleapis.com/css2?family=Lato:wght@300;400;700;900&display=swap" rel="stylesheet">
<style>
  :root {
    --page: #ffffff;
    --grey: #555658;
    --green: #8bc541;
    --white: #ffffff;
  }
  * { margin: 0; padding: 0; box-sizing: border-box; }
  html, body {
    width: 1200px; height: 1200px; overflow: hidden;
    background: var(--page);
    font-family: "Lato", sans-serif;
  }
  .card {
    position: absolute; left: 181px; width: 840px; height: 480px;
    background: var(--grey); overflow: hidden;
  }
  .card--front { top: 70px; }
  .card--back { top: 626px; }

  .brand {
    position: absolute; left: 0; right: 0; top: 0; bottom: 0;
    display: flex; align-items: center; justify-content: center; gap: 26px;
  }
  .brand__dot {
    width: 92px; height: 92px; border-radius: 50%; background: var(--green);
  }
  .brand__name {
    font-weight: 400; font-size: 140px; line-height: 1; color: var(--white);
    letter-spacing: -2px; padding-bottom: 18px;
  }

  .accent-band { position: absolute; left: 0; top: 0; }

  .person { position: absolute; left: 47px; top: 40px; color: var(--white); }
  .person__name {
    font-weight: 700; font-size: 61px; line-height: 1; letter-spacing: -1px;
    text-transform: uppercase;
  }
  .person__title {
    font-weight: 300; font-size: 30px; line-height: 1; margin-top: 16px;
    text-transform: uppercase;
  }

  .contacts { position: absolute; left: 50px; top: 216px; list-style: none; }
  .contact {
    display: flex; align-items: flex-start; height: 84px;
  }
  .contact__icon {
    width: 47px; height: 47px; border: 2px solid var(--green); border-radius: 5px;
    display: flex; align-items: center; justify-content: center; flex-shrink: 0;
  }
  .contact__text {
    margin-left: 31px; margin-top: 0; color: var(--white);
    font-size: 21px; line-height: 26px; font-weight: 400;
  }
</style>
</head>
<body>

<section class="card card--front">
  <div class="brand">
    <span class="brand__dot"></span>
    <span class="brand__name">qorvil</span>
  </div>
</section>

<section class="card card--back">
  <svg class="accent-band" width="840" height="480" viewBox="0 0 840 480" aria-hidden="true">
    <polygon points="450,480 600,160 840,160 840,480" fill="var(--green)"/>
  </svg>

  <header class="person">
    <h1 class="person__name">Olena Dovbush</h1>
    <p class="person__title">Director of Marketing</p>
  </header>

  <ul class="contacts">
    <li class="contact">
      <span class="contact__icon">
        <svg width="26" height="26" viewBox="0 0 24 24" aria-hidden="true">
          <path fill="var(--green)" d="M6.6 10.8c1.4 2.8 3.8 5.1 6.6 6.6l2.2-2.2c.3-.3.7-.4 1-.2 1.1.4 2.3.6 3.6.6.6 0 1 .4 1 1V20c0 .6-.4 1-1 1C10.6 21 3 13.4 3 4c0-.6.4-1 1-1h3.5c.6 0 1 .4 1 1 0 1.3.2 2.5.6 3.6.1.3 0 .7-.2 1z"/>
        </svg>
      </span>
      <p class="contact__text">XXX.XXX.XXXX<br>780.555.0187</p>
    </li>
    <li class="contact">
      <span class="contact__icon">
        <svg width="26" height="26" viewBox="0 0 24 24" aria-hidden="true">
          <circle cx="12" cy="12" r="10" fill="var(--green)"/>
          <path fill="var(--grey)" d="M7 6.5c1.5-.8 3-.6 4 .4l-.5 2-2 .8-.3 2 1.6 1.8-.6 2.5-2-2-1.2-3.5zM14 10l2.5-1 2 1.5.5 3-2 3-1.5-.5.3-2.5-2-1.5z"/>
        </svg>
      </span>
      <p class="contact__text">www.qorvil.example<br>helen.dovbush@mailvane.example</p>
    </li>
    <li class="contact">
      <span class="contact__icon">
        <svg width="26" height="26" viewBox="0 0 24 24" aria-hidden="true">
          <path fill="var(--green)" d="M12 2a7 7 0 0 0-7 7c0 5 7 13 7 13s7-8 7-13a7 7 0 0 0-7-7zm0 9.5A2.5 2.5 0 1 1 12 6.5a2.5 2.5 0 0 1 0 5z"/>
        </svg>
      </span>
      <p class="contact__text">20917 - 87 Ave. Edmonton,<br>&nbsp;AB, Canada. T6K 2R8</p>
    </li>
  </ul>
</section>

</body>
</html>
```